Small but growing painting company. Have built up a steady client base. Want to start having a more professional look. Want to start with changing my business cards, and also getting new logo and tee shirts.

Target Market(s)

Home owners, property management companies, all ages 30-70

Industry/Entity Type

Painting And Decorating

Contact Information for Business Card

Bright Ridge Painting LLC Mark Delvecchi 630-584-3907 interior, exterior, vaulted ceiling, drywall repair, pressure washing, kitchen cabinets, epoxy, garage floors,

Font styles to use
Sans Serif
Other font styles liked:
• Harrington

Colors
0355a3
ffffff
ec1f27
000000
3176b5
0493ce
474747
b7b7b7

Requirements
Must have
• Creative, something that doesn’t look like every other painting card.
Nice to have
• I would like something with an arrow or something going to a point

```html
<!DOCTYPE html>
<html lang="en">
<head>
<meta charset="utf-8">
<title>Bright Ridge Painting LLC — Business Card</title>
<link href="https://fonts.googleapis.com/css2?family=Montserrat:wght@400;500;600;700;800&display=swap" rel="stylesheet">
<style>
  :root {
    --brand-blue: #0355a3;
    --paper: #ffffff;
    --backdrop: #d9dadb;
    --ink-shadow: rgba(0, 0, 0, 0.18);
  }
  * { box-sizing: border-box; margin: 0; padding: 0; }
  html, body {
    width: 1200px; height: 857px; overflow: hidden;
    background: var(--backdrop);
    font-family: "Montserrat", Arial, sans-serif;
  }
  .sheet {
    width: 1200px; height: 857px;
    display: flex; align-items: center; justify-content: center; gap: 60px;
  }
  .card {
    position: relative;
    width: 525px; height: 300px;
    overflow: hidden;
    box-shadow: 0 6px 18px var(--ink-shadow);
  }
  .card--front { background: var(--paper); color: var(--brand-blue); }
  .card--back { background: var(--brand-blue); color: var(--paper); }

  .wordmark {
    font-weight: 700;
    letter-spacing: 0.01em;
    line-height: 1.05;
  }
  .card--front .wordmark {
    position: absolute; left: 42px; top: 70px;
    font-size: 17px;
  }
  .card--back .wordmark {
    position: absolute; left: 0; right: 0; top: 108px;
    text-align: center; font-size: 34px;
  }

  .owner {
    position: absolute; right: 36px; top: 34px; text-align: right;
  }
  .owner__name {
    font-size: 20px; font-weight: 800; letter-spacing: 0.08em;
  }
  .owner__title {
    font-size: 15px; font-weight: 500; margin-top: 6px;
  }

  .phone {
    position: absolute; right: 36px; top: 112px;
    display: flex; align-items: center; gap: 12px;
    font-size: 19px; font-weight: 700; letter-spacing: 0.06em;
  }
  .phone svg { width: 22px; height: 22px; }

  .services {
    position: absolute; left: 42px; top: 148px;
    list-style: none;
    font-size: 11.5px; font-weight: 500; letter-spacing: 0.06em;
    text-transform: uppercase; line-height: 1.55;
  }
  .services li::before {
    content: ""; display: inline-block;
    width: 5px; height: 5px; border-radius: 50%;
    background: var(--brand-blue); margin-right: 7px; vertical-align: middle;
  }
  .services li.services__more { font-weight: 700; }

  .name-tab {
    position: absolute; bottom: 0;
    height: 42px; padding: 0 28px;
    display: flex; align-items: center;
    font-size: 15px; font-weight: 700;
    border-radius: 18px 18px 0 0;
  }
  .card--front .name-tab {
    right: 88px; background: var(--brand-blue); color: var(--paper);
  }
  .card--back .name-tab {
    left: 50%; transform: translateX(-50%);
    background: var(--paper); color: var(--brand-blue);
  }
</style>
</head>
<body>
  <main class="sheet">
    <section class="card card--front" aria-label="Business card front">
      <div class="wordmark">Bright Ridge<br>Painting LLC</div>

      <div class="owner">
        <div class="owner__name">MARK DELVECCHI</div>
        <div class="owner__title">Founder / CEO</div>
      </div>

      <div class="phone">
        <svg viewBox="0 0 24 24" aria-hidden="true">
          <circle cx="12" cy="12" r="10.5" fill="none" stroke="currentColor" stroke-width="2"/>
          <path d="M9.2 7.2c.4-.3.9-.2 1.1.2l.9 1.6c.2.4.1.8-.2 1.1l-.6.5c.5 1.1 1.4 2 2.5 2.6l.5-.6c.3-.3.8-.4 1.1-.2l1.6.9c.4.2.5.8.2 1.1l-.7.9c-.5.6-1.3.8-2 .5-2.6-1.1-4.5-3-5.6-5.6-.3-.7-.1-1.5.5-2z" fill="currentColor"/>
        </svg>
        <span>630-584-3907</span>
      </div>

      <ul class="services">
        <li>Interior | Exterior</li>
        <li>Vaulted Ceiling</li>
        <li>Drywall Repair</li>
        <li>Pressure Washing</li>
        <li class="services__more">And more...</li>
      </ul>

      <div class="name-tab">Bright Ridge Painting LLC</div>
    </section>

    <section class="card card--back" aria-label="Business card back">
      <div class="wordmark">Bright Ridge<br>Painting LLC</div>
      <div class="name-tab">Bright Ridge Painting LLC</div>
    </section>
  </main>
</body>
</html>
```